Website Design for PawRank - New Digital Agency

We are creating a new digital marketing agency and need a new website. I have attached the logo. Our niche is going to be veterinarians. Use the same colors as in the logo (blue, white and gray).

I want real pictures of real people in this and not just boring stock photos. It needs to be related to the industry.

Home page (example:https://linkvorta.com/)
Service page (example: https://darvimosk.com/consulting/)
Case study page (example: https://www.tomaswellbry.com/seo/case-study/)

I will continue to update this brief.
Updates

I updated the brief with some additional sample sites 2 days ago and want to see more designs. I won't need that may more days ...just a few more.

Target Market(s)

veterinarians

Font styles to use
Sans Serif

Requirements
Must have
• I want a very clean looking site. Use the same colors as in the logo (blue, white and gray).
Nice to have
• We need to build this with the idea that the purpose is to generate leads for our business.
• Home page (example:https://linkvorta.com/)
• Service page (example: https://darvimosk.com/consulting/)
• Case study page (example: https://www.tomaswellbry.com/seo/case-study/)

```html
<!DOCTYPE html>
<html lang="en">
<head>
<meta charset="utf-8">
<title>PawRank – Home Page Design</title>
<link href="https://fonts.googleapis.com/css2?family=Raleway:wght@400;500;600;700&family=Open+Sans:wght@400;600;700&display=swap" rel="stylesheet">
<style>
:root{
  --stage:#0f2736;
  --blue:#1653a6;
  --blue-bright:#1e63c0;
  --footer:#1b5cb3;
  --ink:#333a40;
  --muted:#7d858c;
  --soft:#f2f7fc;
  --line:#d9e1e8;
  --white:#ffffff;
}
*{box-sizing:border-box;margin:0;padding:0}
html,body{width:1200px;height:1000px;overflow:hidden}
body{background:var(--stage);font-family:"Open Sans",sans-serif;color:var(--ink);position:relative}
.page-frame{position:absolute;left:475px;top:10px;width:250px;height:980px;overflow:hidden;background:var(--white)}
.page{width:500px;transform:scale(.5);transform-origin:0 0}
h1,h2,h3,h4{font-family:"Raleway",sans-serif;font-weight:500}
p{font-size:5.5px;line-height:1.6;color:var(--muted)}

/* top bar */
.topbar{height:14px;background:#4a4f55;display:flex;align-items:center;justify-content:space-between;padding:0 40px;font-size:4.5px;color:#e5e7ea}
.topbar .contacts{display:flex;gap:12px}
.topbar .social{display:flex;gap:4px}
.topbar .social i{width:5px;height:5px;border-radius:50%;background:#e5e7ea;display:block}

/* header */
.site-header{height:46px;display:flex;align-items:center;justify-content:space-between;padding:0 40px}
.brand{display:flex;align-items:center;gap:4px;font-family:"Raleway",sans-serif;font-weight:700;font-size:16px;color:var(--blue)}
.brand .dot{width:7px;height:7px;border-radius:50%;background:var(--blue)}
.main-nav{display:flex;gap:9px;font-family:"Raleway",sans-serif;font-weight:700;font-size:5px;color:var(--blue);align-items:center}
.main-nav svg{width:7px;height:7px}

/* hero */
.hero{height:290px;position:relative;background:linear-gradient(180deg,#fafafa,#f1f1f1)}
.hero-copy{position:absolute;left:56px;top:44px;width:190px}
.hero-copy h1{font-size:19px;line-height:1.05;color:var(--blue);font-weight:500}
.hero-copy h1 strong{display:block;font-size:26px;color:var(--ink);font-weight:700;margin-top:2px}
.hero-copy p{margin-top:8px;width:170px}
.btn{display:inline-block;background:var(--blue);color:var(--white);font-family:"Raleway",sans-serif;font-weight:700;font-size:5px;padding:6px 12px;margin-top:10px}
.hero-photo{position:absolute;left:248px;top:0;width:200px;height:290px;background:linear-gradient(180deg,#f3f3f3 0%,#dcdfe3 40%,#6e7887 70%,#3a4658 100%)}

/* welcome */
.welcome{height:226px;text-align:center;padding-top:60px}
.eyebrow{font-family:"Raleway",sans-serif;font-weight:700;font-size:6px;color:var(--ink);letter-spacing:.3px}
.section-title{font-size:14px;color:var(--blue);margin-top:3px}
.rule{width:26px;height:1.5px;background:var(--blue);margin:7px auto}
.welcome p{width:330px;margin:8px auto 0}

/* services */
.services{height:296px;background:var(--soft);text-align:center;padding-top:22px}
.services .section-title{font-size:16px}
.services > p{width:330px;margin:8px auto 0}
.service-board{margin:14px 44px 0;background:var(--white);height:190px;display:flex;justify-content:space-around;padding-top:14px}
.service{width:110px;display:flex;flex-direction:column;align-items:center}
.service .icon{width:26px;height:26px;border:1.5px solid var(--blue);border-radius:50%;display:flex;align-items:center;justify-content:center}
.service .icon svg{width:14px;height:14px}
.service h3{font-family:"Open Sans",sans-serif;font-weight:700;font-size:5.5px;color:var(--ink);margin-top:8px;line-height:1.3}
.service p{margin-top:5px}
.read-more{margin-top:9px;border:1px solid var(--line);font-size:4.5px;padding:3px 9px;color:var(--ink)}

/* mission */
.mission{height:152px;position:relative;text-align:center;color:var(--white)}
.mission .bg{position:absolute;inset:0;background:linear-gradient(100deg,#3a3f45,#5b6066 45%,#2d3136)}
.mission .copy{position:relative;padding-top:54px}
.mission h2{font-size:14px;line-height:1.2;color:var(--white)}
.mission .by{font-size:5px;font-weight:700;margin-top:9px}

/* clients */
.clients{height:62px;background:#f6f7f8;display:flex;align-items:center;justify-content:space-around;padding:0 40px;font-family:"Raleway",sans-serif;font-weight:700;font-size:8px;color:#aeb4ba}

/* about */
.about{height:300px;display:flex;padding:30px 44px 0;gap:24px}
.about-copy{width:190px}
.about-copy h2{font-size:12px;line-height:1.15;color:var(--blue);font-weight:700}
.about-copy .rule{margin:6px 0}
.about-copy p{margin-bottom:6px}
.checks{list-style:none;font-size:5px;color:var(--muted)}
.checks li{display:flex;align-items:center;gap:5px;margin-bottom:4px}
.checks li::before{content:"";width:6px;height:6px;border-radius:50%;background:var(--blue)}
.about-stats{flex:1;padding-top:4px}
.skill{margin-bottom:9px}
.skill .label{display:flex;justify-content:space-between;font-size:4.5px;color:var(--ink);width:170px}
.skill .track{height:3px;background:#e3e8ee;margin-top:2px;width:170px}
.skill .fill{height:100%;background:var(--blue-bright)}
.chart{width:190px;height:140px;margin-top:6px}

/* testimonials */
.testimonials{height:228px;position:relative;text-align:center;color:var(--white)}
.testimonials .bg{position:absolute;inset:0;background:linear-gradient(90deg,#2f3338,#4a4d52 50%,#35393e)}
.testimonials .copy{position:relative;padding-top:30px}
.testimonials .eyebrow{color:var(--white);font-weight:500}
.testimonials h2{font-size:14px;color:var(--white)}
.testimonials p{width:340px;margin:14px auto 0;color:#dfe2e5}
.avatar{width:24px;height:24px;border-radius:50%;background:linear-gradient(135deg,#b2507a,#6d2a4a);margin:12px auto 0;border:1.5px solid var(--white)}
.reviewer{font-size:5px;font-weight:700;margin-top:5px}
.reviewer-role{font-size:4.5px;color:#cfd3d7}

/* portfolio */
.portfolio{height:238px;text-align:center;padding-top:22px}
.portfolio .section-title{font-size:16px}
.portfolio-grid{margin-top:18px;height:152px;background:linear-gradient(100deg,#c9dced,#e7eef5 30%,#a9bccd 55%,#dfe8f1 80%,#b7c6d4)}

/* footer */
.site-footer{height:136px;background:var(--footer);color:var(--white);padding:12px 44px 0}
.footer-cols{display:flex;gap:26px}
.footer-cols h4{font-family:"Open Sans",sans-serif;font-weight:700;font-size:5.5px}
.footer-cols ul{list-style:none;font-size:4.5px;line-height:1.8;margin-top:4px;color:#d8e4f4;columns:2;column-gap:12px}
.col-offer{width:110px}
.col-info{width:70px}
.col-news p{color:#d8e4f4;font-size:4.5px;margin-top:4px}
.subscribe{display:flex;margin-top:5px}
.subscribe span{width:90px;height:9px;background:var(--white)}
.subscribe b{background:#0f3f80;font-size:4px;padding:2px 6px;line-height:5px}
.footer-bar{display:flex;align-items:center;justify-content:space-between;margin-top:26px;font-size:4.5px;color:#d8e4f4}
.footer-bar .brand{color:var(--white);font-size:12px}
.footer-bar .brand .dot{background:var(--white);width:5px;height:5px}
.footer-bar .social{display:flex;gap:4px}
.footer-bar .social i{width:5px;height:5px;border-radius:50%;background:var(--white);display:block}
.copyright{text-align:center;font-size:4px;color:#c6d6ec;margin-top:14px}
</style>
</head>
<body>
<div class="page-frame">
<div class="page">

  <div class="topbar">
    <div class="contacts"><span>48 Harbor Lane, Eastfield</span><span>hello@pawrank.com</span><span>+100 0555 01 22</span></div>
    <div class="social"><i></i><i></i><i></i><i></i></div>
  </div>

  <header class="site-header">
    <div class="brand"><span class="dot"></span>PawRank</div>
    <nav class="main-nav">
      <span>HOME</span><span>ABOUT</span><span>SERVICES</span><span>TEAM</span><span>BLOG</span><span>PAGES</span><span>CONTACTS</span>
      <svg viewBox="0 0 10 10"><circle cx="4" cy="4" r="3" fill="none" stroke="#333a40" stroke-width="1.2"/><line x1="6.3" y1="6.3" x2="9" y2="9" stroke="#333a40" stroke-width="1.2"/></svg>
    </nav>
  </header>

  <section class="hero">
    <div class="hero-copy">
      <h1>SEO HELP YOUR<br>BUSINESS BECOME<strong>SUCCESSFUL</strong></h1>
      <p>Lorem Ipsum is simply dummy text of the printing and typesetting industry. Lorem Ipsum has been the industry's standard dummy text ever since the 1500s.</p>
      <span class="btn">GET IN TOUCH</span>
    </div>
    <div class="hero-photo" role="img" aria-label="Photo of a smiling man in a dark blazer and white shirt"></div>
  </section>

  <section class="welcome">
    <div class="eyebrow">WELCOME TO PAWRANK</div>
    <h2 class="section-title">WHAT WE DO FOR YOUR SUCCESS</h2>
    <div class="rule"></div>
    <p>Lorem Ipsum is simply dummy text of the printing and typesetting industry. Lorem Ipsum has been the industry's standard dummy text ever since the 1500s, when an unknown printer took a galley of type and scrambled it to make a type specimen book. It has survived not only five centuries, but also the leap into electronic typesetting, remaining essentially unchanged.</p>
  </section>

  <section class="services">
    <h2 class="section-title">OUR SERVICES</h2>
    <p>Lorem Ipsum is simply dummy text of the printing and typesetting industry. Lorem Ipsum has been the industry's standard dummy text ever since the 1500s.</p>
    <div class="service-board">
      <div class="service">
        <div class="icon"><svg viewBox="0 0 14 14"><rect x="1" y="2" width="10" height="7" fill="none" stroke="#1653a6"/><circle cx="8" cy="8" r="2.5" fill="#fff" stroke="#1653a6"/><line x1="10" y1="10" x2="13" y2="13" stroke="#1653a6"/></svg></div>
        <h3>SEARCH ENGINE<br>OPTIMIZATION</h3>
        <p>Lorem Ipsum is simply dummy text of the printing and typesetting industry. Lorem Ipsum has been the industry's standard dummy text ever since the 1500s.</p>
        <span class="read-more">Read More</span>
      </div>
      <div class="service">
        <div class="icon"><svg viewBox="0 0 14 14"><rect x="1" y="3" width="12" height="8" fill="#1653a6"/><polyline points="1,3 7,8 13,3" fill="none" stroke="#fff"/></svg></div>
        <h3>EMAIL MARKETING<br>SERVICES</h3>
        <p>Lorem Ipsum is simply dummy text of the printing and typesetting industry. Lorem Ipsum has been the industry's standard dummy text ever since the 1500s.</p>
        <span class="read-more">Read More</span>
      </div>
      <div class="service">
        <div class="icon"><svg viewBox="0 0 14 14"><polygon points="2,5 6,5 11,2 11,12 6,9 2,9" fill="#1653a6"/><rect x="4" y="9" width="2" height="3" fill="#1653a6"/></svg></div>
        <h3>PPC/PAY-PER-CLICK<br>CAMPAIGNS</h3>
        <p>Lorem Ipsum is simply dummy text of the printing and typesetting industry. Lorem Ipsum has been the industry's standard dummy text ever since the 1500s.</p>
        <span class="read-more">Read More</span>
      </div>
    </div>
  </section>

  <section class="mission">
    <div class="bg" role="img" aria-label="Dark photo of hands working at a desk"></div>
    <div class="copy">
      <h2>OUR MISSION IS TO MAKE THE<br>BUSINESS LIFE OF OUR CLIENTS BETTER!</h2>
      <div class="by">ALDEN ROOK, FOUNDER</div>
    </div>
  </section>

  <section class="clients">
    <span>NORDVALE</span><span>quillo</span><span>IBORA</span><span>helmcrest</span><span>Marlow</span><span>SOTIKA</span>
  </section>

  <section class="about">
    <div class="about-copy">
      <h2>A FEW WORDS<br>ABOUT OUR AGENCY</h2>
      <div class="rule"></div>
      <p>We're an international marketing agency that blends creative technologies and consultants into one unified service that helps clinics grow, reach pet owners and win trust across every channel online.</p>
      <p>Our range of services covers search, email, paid ads and content. Whatever your needs, we deliver clear results and long term growth for your practice.</p>
      <p>Since our establishment we have helped many practices increase their profit.</p>
      <ul class="checks">
        <li>2016 – 180% companies</li>
        <li>2015 – 150% companies</li>
        <li>2014 – 130% companies</li>
        <li>2013 – 110% companies</li>
        <li>2012 – 90% companies</li>
      </ul>
    </div>
    <div class="about-stats">
      <div class="skill"><div class="label"><span>LOCAL SEO</span><span>90%</span></div><div class="track"><div class="fill" style="width:90%"></div></div></div>
      <div class="skill"><div class="label"><span>PPC</span><span>75%</span></div><div class="track"><div class="fill" style="width:75%"></div></div></div>
      <div class="skill"><div class="label"><span>EMAIL</span><span>60%</span></div><div class="track"><div class="fill" style="width:60%"></div></div></div>
      <svg class="chart" viewBox="0 0 190 140">
        <g stroke="#e6ebf0" stroke-width=".6">
          <line x1="10" y1="20" x2="185" y2="20"/><line x1="10" y1="50" x2="185" y2="50"/><line x1="10" y1="80" x2="185" y2="80"/><line x1="10" y1="110" x2="185" y2="110"/>
        </g>
        <rect x="14" y="80" width="5" height="40" fill="#f06a6a"/>
        <rect x="24" y="58" width="5" height="62" fill="#8d6ff0"/>
        <rect x="40" y="70" width="5" height="50" fill="#f06a6a"/>
        <rect x="50" y="44" width="5" height="76" fill="#5e7ff0"/>
        <rect x="66" y="62" width="5" height="58" fill="#3ed2a0"/>
        <rect x="76" y="50" width="5" height="70" fill="#8d6ff0"/>
        <rect x="92" y="74" width="5" height="46" fill="#3ed2a0"/>
        <rect x="102" y="30" width="5" height="90" fill="#8d6ff0"/>
        <rect x="118" y="64" width="5" height="56" fill="#3ed2a0"/>
        <rect x="128" y="38" width="5" height="82" fill="#5e7ff0"/>
        <rect x="144" y="56" width="5" height="64" fill="#8d6ff0"/>
        <rect x="160" y="100" width="5" height="20" fill="#f06a6a"/>
        <line x1="10" y1="120" x2="185" y2="120" stroke="#c9d1d9" stroke-width=".8"/>
        <g font-size="4" fill="#7d858c" font-family="Open Sans, sans-serif">
          <text x="16" y="128">2012</text><text x="44" y="128">2013</text><text x="70" y="128">2014</text><text x="98" y="128">2015</text><text x="124" y="128">2016</text><text x="150" y="128">2017</text>
        </g>
      </svg>
    </div>
  </section>

  <section class="testimonials">
    <div class="bg" role="img" aria-label="Dim photo of a woman working on a laptop"></div>
    <div class="copy">
      <div class="eyebrow">WE ENJOY WORKING</div>
      <h2>WHAT PEOPLE SAY</h2>
      <p>Lorem Ipsum is simply dummy text of the printing and typesetting industry. Lorem Ipsum has been the industry's standard dummy text ever since the 1500s, when an unknown printer took a galley of type and scrambled it to make a type specimen book. It has survived not only five centuries, but also the leap into electronic typesetting.</p>
      <div class="avatar" role="img" aria-label="Portrait of the client"></div>
      <div class="reviewer">MARTA KELLEN</div>
      <div class="reviewer-role">VP Sales and Marketing</div>
    </div>
  </section>

  <section class="portfolio">
    <h2 class="section-title">OUR PORTFOLIO</h2>
    <div class="rule"></div>
    <div class="portfolio-grid" role="img" aria-label="Grid of office and team photos from client projects"></div>
  </section>

  <footer class="site-footer">
    <div class="footer-cols">
      <div class="col-offer">
        <h4>What We Offer</h4>
        <ul><li>Reputation Mgmt</li><li>PPC Services</li><li>Email Marketing</li><li>Conversion Opt.</li><li>Local Marketing</li><li>Website Design</li></ul>
      </div>
      <div class="col-info">
        <h4>Information</h4>
        <ul><li>About us</li><li>Latest News</li><li>Our Work</li><li>FAQ</li><li>Blog</li><li>Contacts</li></ul>
      </div>
      <div class="col-news">
        <h4>Newsletter</h4>
        <p>Sign up today for the latest news and tips</p>
        <div class="subscribe"><span></span><b>SUBSCRIBE</b></div>
      </div>
    </div>
    <div class="footer-bar">
      <div class="brand"><span class="dot"></span>PawRank</div>
      <span>48 Harbor Lane, Eastfield</span>
      <span>hello@pawrank.com</span>
      <span>+100 0555 01 22</span>
      <div class="social"><i></i><i></i><i></i><i></i></div>
    </div>
    <div class="copyright">© 2024 PawRank. All rights reserved</div>
  </footer>

</div>
</div>
</body>
</html>
```